Modern claims management company

We need a new company presentation brochure, composed of about 20 pages in A4 format.
Cover, page 1 who we are, page 2 company profile, page 3 territorial operation, page from 4 to 10 services offered and description of services (The title of the page are: Perizie e Liquidazione danni, riparazioni e sostituzioni, teleclaimer, accertamento danni da fenomeno elettrico, TPA, Auditing, drone pilot, Valutazione rischi), from 11 to 17 specializations (Sinistri gravi, R.C., Tecnologici, Energie rinnovabili, strutture, ambiente) page 18 e 19 integrated services (perdite occulte, ricerca guasti, indagini termografiche, crisis management), page 20 clients ( list companies and logos) page 21 contact.
The company is made up of various companies, which belong to the principal, each of which deals with specific activities.
To date we already have various logos of the main company (Tavesi and Durando) as well as the logos of the other companies. I load them on the portal.
Found then the graphic solution that we like we will have to proceed to make a presentation in similar powerpoint and the website.

Target Market(s)

Insurance Company, Insurance Broker

Other font styles liked:
• ARIAL

Colors
333333
5c5c5c
959595
0392cd

Requirements
Must have
• It must be clear, professional and modern.
Nice to have
• I indicate some competitor sites, so that you can better understand what we are doing. www.fenwoodhale.com, www.harrowpikestead.com, www.orsavantini.com, www.gruppotessandi.com, www.vandrini.eu.

```html
<!DOCTYPE html>
<html lang="it">
<head>
<meta charset="utf-8">
<title>Tavesi and Durando – Brochure</title>
<link href="https://fonts.googleapis.com/css2?family=Arimo:wght@400;700&display=swap" rel="stylesheet">
<style>
:root{
  --blue:#0392cd;
  --orange:#f47c20;
  --ink:#333333;
  --mid:#5c5c5c;
  --soft:#959595;
  --line:#e3e3e3;
  --board:#f1f1f1;
  --dark:#3b3b3b;
}
*{box-sizing:border-box;margin:0;padding:0}
html,body{width:1200px;height:2305px;overflow:hidden}
body{background:var(--board);font-family:"Arimo",Arial,sans-serif;color:var(--ink);position:relative}
.spread{position:absolute;width:547px;height:355px;background:#fff;box-shadow:0 0 2px rgba(0,0,0,.18)}
.page{position:absolute;top:0;width:273px;height:355px;overflow:hidden}
.page.left{left:0;border-right:1px solid var(--line)}
.page.right{left:274px}
.mark{position:absolute;top:2px;right:8px;font-size:21px;font-weight:700;color:#ececec;letter-spacing:.5px;white-space:nowrap}
.page.left .mark{right:auto;left:140px}
.title{position:absolute;font-size:9px;font-weight:700;color:var(--orange);text-transform:uppercase;letter-spacing:.2px;white-space:nowrap}
.title.small{font-size:7.4px}
.band{position:absolute;background:var(--blue);color:#fff}
.band.title-band{font-size:9px;font-weight:700;padding:10px 14px;text-transform:uppercase;white-space:nowrap}
.photo{position:absolute}
.box{position:absolute;padding:6px;font-size:4.6px;line-height:1.35;color:#fff}
.box.orange{background:var(--orange)}
.box.blue{background:var(--blue)}
.intro{position:absolute;font-size:4.6px;line-height:1.35;color:var(--blue)}
.col{position:absolute;width:80px}
.col p{font-size:3.9px;line-height:1.4;color:var(--mid);margin-bottom:4px}
.col p.lead{font-weight:700;color:var(--ink)}
.col.on-blue p{color:#fff}
.foot{position:absolute;left:0;right:0;bottom:0;height:14px;border-top:1px solid var(--blue);font-size:3.6px;color:var(--soft);display:flex;align-items:center;justify-content:space-between;padding:0 10px}
.foot .brand{font-size:4.6px;font-weight:700;color:var(--blue)}
.foot .num{color:#fff;background:var(--blue);padding:1px 2px}
/* cover */
.cover{position:absolute;left:312px;top:30px;width:576px;height:345px;background:#fff;box-shadow:0 0 2px rgba(0,0,0,.18)}
.cover .half{position:absolute;top:0;width:288px;height:345px;overflow:hidden}
.cover h2{position:absolute;left:14px;top:10px;font-size:8px;color:var(--orange)}
.unit{position:absolute;width:120px}
.unit .name{font-size:7px;font-weight:700;color:var(--blue);display:flex;align-items:center;gap:3px;white-space:nowrap}
.unit .name i{display:inline-block;width:6px;height:6px;background:var(--orange)}
.unit h3{font-size:4.8px;color:var(--orange);margin:5px 0 3px}
.unit li{font-size:3.8px;line-height:1.4;color:var(--mid);margin-left:6px}
.badges{position:absolute;left:28px;top:270px;display:flex;gap:34px}
.badges span{width:22px;height:14px;background:#d5d9de;border-radius:2px}
.badges span:first-child{border-radius:50%;width:14px}
.cover-foot{position:absolute;left:0;right:0;bottom:0;height:22px;background:var(--blue);font-size:3.6px;color:#fff;display:flex;align-items:center;gap:40px;padding:0 14px}
.cover .logos{position:absolute;top:14px;right:14px;display:flex;gap:10px;font-size:6.5px;font-weight:700;color:var(--blue);white-space:nowrap}
.cover .titles{position:absolute;left:16px;top:205px;color:#fff;font-size:7px;font-weight:700;line-height:1.3}
.cover .titles p{margin-bottom:8px}
.cover .site{position:absolute;right:14px;bottom:16px;font-size:5px;color:#fff}
.stripe{position:absolute;left:0;right:0;bottom:0;height:10px;background:linear-gradient(90deg,var(--blue) 0 60%,var(--orange) 60% 100%)}
/* clients */
.clients{position:absolute;left:12px;top:30px;width:250px;display:grid;grid-template-columns:repeat(4,1fr);gap:8px 6px}
.clients span{font-size:6.4px;font-weight:700;color:var(--ink);height:16px;display:flex;align-items:center}
</style>
</head>
<body>

<div class="cover">
  <div class="half" style="left:0">
    <h2>LA STRUTTURA</h2>
    <div class="unit" style="left:14px;top:30px">
      <div class="name"><i></i>Tavesi and Durando</div>
      <h3>Divisione sinistri Property e Liability</h3>
      <ul><li>Gestione perizie rami elementari con rete nazionale</li><li>Consulenza tecnica e liquidazione per compagnie e broker</li></ul>
    </div>
    <div class="unit" style="left:150px;top:30px">
      <div class="name"><i></i>Riparo Servizi</div>
      <h3>Indennizzo in forma specifica</h3>
      <ul><li>Riparazioni dirette con personale interno e artigiani</li><li>Operatori con rete fornitori per la gestione dei sinistri</li></ul>
    </div>
    <div class="unit" style="left:14px;top:135px">
      <div class="name"><i></i>Fulgora</div>
      <h3>Sinistri da Fenomeno Elettrico</h3>
      <ul><li>Verifica tecnica dei danni da fenomeno elettrico</li><li>Laboratorio interno e tecnici certificati sul territorio</li></ul>
    </div>
    <div class="unit" style="left:150px;top:135px">
      <div class="name"><i></i>Resolva</div>
      <h3>Servizi integrati</h3>
      <ul><li>Teleclaimer</li><li>Crisis Management</li><li>Auditing</li><li>Energie rinnovabili</li><li>A.P.R. (Droni)</li><li>Valutazione rischi</li><li>Tecnologici</li><li>Business interruption</li></ul>
    </div>
    <div class="badges"><span></span><span></span><span></span><span></span></div>
    <div class="cover-foot"><span>Via Roma 12 – 40100 Bologna</span><span>Via Verdi 8 – 20100 Milano</span></div>
  </div>
  <div class="half" style="left:288px;background:var(--dark)">
    <div style="position:absolute;left:0;top:0;width:288px;height:48px;background:#fff"></div>
    <div class="logos"><span>Tavesi and Durando</span><span>Riparo Servizi</span><span>Fulgora</span></div>
    <div class="photo" role="img" aria-label="Primo piano di una tastiera e documenti in bianco e nero" style="left:0;top:48px;width:288px;height:130px;background:linear-gradient(135deg,#1b1b1b,#6d6d6d 55%,#2a2a2a)"></div>
    <div class="titles">
      <p>PERIZIE ASSICURATIVE</p>
      <p>INDENNIZZO IN FORMA SPECIFICA</p>
      <p>ACCERTAMENTO DANNI DA<br>FENOMENO ELETTRICO</p>
    </div>
    <div class="site">www.tavesidurando.it</div>
    <div class="stripe"></div>
  </div>
</div>

<div class="spread" style="left:38px;top:402px">
  <div class="page left">
    <div class="photo" role="img" aria-label="Mani sovrapposte in segno di squadra" style="left:0;top:12px;width:160px;height:82px;background:linear-gradient(135deg,#c8b8a6,#7b6a5c)"></div>
    <div class="box orange" style="left:160px;top:30px;width:113px;height:78px">Our adjusters examine each loss on site, gather the facts and prepare a clear report, so insurers and brokers can settle the claim quickly and fairly for every client.</div>
    <div class="title" style="left:12px;top:112px">WHO WE ARE</div>
    <div class="col" style="left:12px;top:126px;width:118px"><p>Our adjusters examine each loss on site, gather the facts and prepare a clear report, so insurers and brokers can settle the claim quickly and fairly for every client.</p><p>Every file is followed by a dedicated expert and tracked in real time.</p><p>Our adjusters examine each loss on site, gather the facts and prepare a clear report, so insurers and brokers can settle the claim quickly and fairly for every client.</p></div>
    <div class="col" style="left:142px;top:126px;width:118px"><p>Our adjusters examine each loss on site, gather the facts and prepare a clear report, so insurers and brokers can settle the claim quickly and fairly for every client.</p><p class="lead">Fast, precise assessments with a single contact from the first notice to the final settlement.</p><p>Every file is followed by a dedicated expert and tracked in real time.</p></div>
    <div class="foot"><span class="num">01</span><span>www.tavesidurando.it</span><span class="brand">Tavesi and Durando</span></div>
  </div>
  <div class="page right">
    <div class="band title-band" style="left:0;top:14px;width:273px">COMPANY PROFILE</div>
    <div class="photo" role="img" aria-label="Riunione di lavoro in ufficio luminoso" style="left:12px;top:44px;width:130px;height:70px;background:linear-gradient(135deg,#dfe6ec,#8d9aa6)"></div>
    <div class="col" style="left:150px;top:46px;width:112px"><p class="lead">Fast, precise assessments with a single contact from the first notice to the final settlement.</p><p>Our adjusters examine each loss on site, gather the facts and prepare a clear report, so insurers and brokers can settle the claim quickly and fairly for every client.</p></div>
    <div class="col" style="left:12px;top:124px;width:125px"><p>Our adjusters examine each loss on site, gather the facts and prepare a clear report, so insurers and brokers can settle the claim quickly and fairly for every client.</p><p class="lead">Fast, precise assessments with a single contact from the first notice to the final settlement.</p><p>Every file is followed by a dedicated expert and tracked in real time.</p></div>
    <div class="col" style="left:150px;top:124px;width:112px"><p>Our adjusters examine each loss on site, gather the facts and prepare a clear report, so insurers and brokers can settle the claim quickly and fairly for every client.</p><p>Every file is followed by a dedicated expert and tracked in real time.</p></div>
    <div class="foot"><span class="brand">Tavesi and Durando</span><span>www.tavesidurando.it</span><span class="num">02</span></div>
  </div>
</div>

<div class="spread" style="left:608px;top:402px">
  <div class="page left">
    <div class="mark" style="left:50px">SPECIALIZATIONS</div>
    <div class="title" style="left:12px;top:26px">SINISTRI GRAVI</div>
    <div class="photo" role="img" aria-label="Soccorritori intorno a una barella" style="left:12px;top:40px;width:250px;height:85px;background:linear-gradient(135deg,#c9a27e,#4a5f78)"></div>
    <div class="intro" style="left:12px;top:130px;width:250px">Fast, precise assessments with a single contact from the first notice to the final settlement.</div>
    <div class="col" style="left:12px;top:148px;width:118px"><p>Our adjusters examine each loss on site, gather the facts and prepare a clear report, so insurers and brokers can settle the claim quickly and fairly for every client.</p><p class="lead">Fast, precise assessments with a single contact from the first notice to the final settlement.</p><p>Every file is followed by a dedicated expert and tracked in real time.</p></div>
    <div class="col" style="left:142px;top:148px;width:118px"><p class="lead">Fast, precise assessments with a single contact from the first notice to the final settlement.</p><p>Our adjusters examine each loss on site, gather the facts and prepare a clear report, so insurers and brokers can settle the claim quickly and fairly for every client.</p></div>
    <div class="foot"><span class="num">11</span><span>www.tavesidurando.it</span><span class="brand">Tavesi and Durando</span></div>
  </div>
  <div class="page right">
    <div class="mark">SPECIALIZATIONS</div>
    <div class="photo" role="img" aria-label="Persona a terra dopo un incidente" style="left:12px;top:40px;width:120px;height:85px;background:linear-gradient(135deg,#d9d2c8,#8a7e70)"></div>
    <div class="col" style="left:140px;top:40px;width:120px"><p>Our adjusters examine each loss on site, gather the facts and prepare a clear report, so insurers and brokers can settle the claim quickly and fairly for every client.</p></div>
    <div class="intro" style="left:12px;top:130px;width:250px">Fast, precise assessments with a single contact from the first notice to the final settlement.</div>
    <div class="col" style="left:12px;top:148px;width:118px"><p>Our adjusters examine each loss on site, gather the facts and prepare a clear report, so insurers and brokers can settle the claim quickly and fairly for every client.</p></div>
    <div class="photo" role="img" aria-label="Dettaglio di una mano ferita" style="left:140px;top:150px;width:50px;height:60px;background:linear-gradient(135deg,#b58d7a,#5a3f38)"></div>
    <div class="col" style="left:196px;top:150px;width:66px"><p>Every file is followed by a dedicated expert and tracked in real time.</p></div>
    <div class="foot"><span class="brand">Tavesi and Durando</span><span>www.tavesidurando.it</span><span class="num">12</span></div>
  </div>
</div>

<div class="spread" style="left:38px;top:772px">
  <div class="page left">
    <div class="band title-band" style="left:0;top:10px;width:172px">TERRITORIAL OPERATION</div>
    <div class="photo" role="img" aria-label="Mappa dell'Europa con le aree di intervento" style="left:12px;top:40px;width:140px;height:82px;background:linear-gradient(135deg,#e8eef2,#b9c6d0)"></div>
    <div class="col" style="left:12px;top:128px;width:118px"><p>Our adjusters examine each loss on site, gather the facts and prepare a clear report, so insurers and brokers can settle the claim quickly and fairly for every client.</p><p>Every file is followed by a dedicated expert and tracked in real time.</p></div>
    <div class="box orange" style="left:12px;top:200px;width:118px;height:70px">Our adjusters examine each loss on site, gather the facts and prepare a clear report, so insurers and brokers can settle the claim.</div>
    <div class="col" style="left:142px;top:128px;width:120px"><p class="lead">Fast, precise assessments with a single contact from the first notice to the final settlement.</p><p>Our adjusters examine each loss on site, gather the facts and prepare a clear report, so insurers and brokers can settle the claim quickly and fairly for every client.</p><p>Every file is followed by a dedicated expert and tracked in real time.</p></div>
    <div class="foot"><span class="num">03</span><span>www.tavesidurando.it</span><span class="brand">Tavesi and Durando</span></div>
  </div>
  <div class="page right">
    <div class="mark">SERVICES</div>
    <div class="title" style="left:12px;top:30px">PERIZIE E LIQUIDAZIONE DANNI</div>
    <div class="photo" role="img" aria-label="Perito che compila un modulo" style="left:12px;top:44px;width:120px;height:80px;background:linear-gradient(135deg,#cfd6dc,#6f7c88)"></div>
    <div class="col" style="left:140px;top:44px;width:122px"><p>Our adjusters examine each loss on site, gather the facts and prepare a clear report, so insurers and brokers can settle the claim quickly and fairly for every client.</p><p class="lead">Fast, precise assessments with a single contact from the first notice to the final settlement.</p></div>
    <div class="col" style="left:12px;top:132px;width:118px"><p>Our adjusters examine each loss on site, gather the facts and prepare a clear report, so insurers and brokers can settle the claim quickly and fairly for every client.</p><p class="lead">Fast, precise assessments with a single contact from the first notice to the final settlement.</p><p>Every file is followed by a dedicated expert and tracked in real time.</p></div>
    <div class="col" style="left:140px;top:132px;width:122px"><p class="lead">Fast, precise assessments with a single contact from the first notice to the final settlement.</p><p>Our adjusters examine each loss on site, gather the facts and prepare a clear report, so insurers and brokers can settle the claim quickly and fairly for every client.</p></div>
    <div class="foot"><span class="brand">Tavesi and Durando</span><span>www.tavesidurando.it</span><span class="num">04</span></div>
  </div>
</div>

<div class="spread" style="left:608px;top:772px">
  <div class="page left">
    <div class="mark" style="left:50px">SPECIALIZATIONS</div>
    <div class="title" style="left:12px;top:26px">R.C.</div>
    <div class="photo" role="img" aria-label="Auto sportiva" style="left:12px;top:40px;width:120px;height:75px;background:linear-gradient(135deg,#3f5a6a,#b6c2c8)"></div>
    <div class="box orange" style="left:132px;top:52px;width:130px;height:60px">Our adjusters examine each loss on site, gather the facts and prepare a clear report for every client.</div>
    <div class="photo" role="img" aria-label="Modellino di fuoristrada radiocomandato" style="left:140px;top:120px;width:120px;height:70px;background:linear-gradient(135deg,#f4f4f4,#8c98a6)"></div>
    <div class="intro" style="left:12px;top:122px;width:120px">Fast, precise assessments with a single contact from the first notice.</div>
    <div class="col" style="left:12px;top:140px;width:118px"><p>Our adjusters examine each loss on site, gather the facts and prepare a clear report, so insurers and brokers can settle the claim quickly and fairly for every client.</p><p class="lead">Fast, precise assessments with a single contact from the first notice to the final settlement.</p></div>
    <div class="col" style="left:140px;top:198px;width:120px"><p>Our adjusters examine each loss on site, gather the facts and prepare a clear report, so insurers and brokers can settle the claim quickly and fairly for every client.</p></div>
    <div class="foot"><span class="num">13</span><span>www.tavesidurando.it</span><span class="brand">Tavesi and Durando</span></div>
  </div>
  <div class="page right">
    <div class="mark">SPECIALIZATIONS</div>
    <div class="title" style="left:140px;top:26px">ENERGIE RINNOVABILI</div>
    <div class="box blue" style="left:12px;top:40px;width:120px;height:60px">Our adjusters examine each loss on site, gather the facts and prepare a clear report for every client.</div>
    <div class="photo" role="img" aria-label="Pannelli solari e globo verde" style="left:140px;top:40px;width:122px;height:75px;background:linear-gradient(135deg,#8bc34a,#2f6d8f)"></div>
    <div class="col" style="left:12px;top:108px;width:118px"><p class="lead">Fast, precise assessments with a single contact from the first notice to the final settlement.</p><p>Our adjusters examine each loss on site, gather the facts and prepare a clear report.</p></div>
    <div class="photo" role="img" aria-label="Turbine eoliche al tramonto" style="left:12px;top:160px;width:120px;height:60px;background:linear-gradient(135deg,#3f7fb5,#d7e6f0)"></div>
    <div class="col" style="left:140px;top:124px;width:122px"><p>Our adjusters examine each loss on site, gather the facts and prepare a clear report, so insurers and brokers can settle the claim quickly and fairly for every client.</p></div>
    <div class="col" style="left:12px;top:228px;width:250px"><p>Our adjusters examine each loss on site, gather the facts and prepare a clear report, so insurers and brokers can settle the claim quickly and fairly for every client.</p></div>
    <div class="foot"><span class="brand">Tavesi and Durando</span><span>www.tavesidurando.it</span><span class="num">14</span></div>
  </div>
</div>

<div class="spread" style="left:38px;top:1140px">
  <div class="page left">
    <div class="mark">SERVICES</div>
    <div class="title" style="left:12px;top:26px">RIPARAZIONI E SOSTITUZIONI</div>
    <div class="photo" role="img" aria-label="Tecnico al lavoro con attrezzi" style="left:12px;top:40px;width:250px;height:75px;background:linear-gradient(135deg,#6c7a4f,#c9cfc0)"></div>
    <div class="intro" style="left:12px;top:120px;width:250px">Fast, precise assessments with a single contact from the first notice to the final settlement.</div>
    <div class="col" style="left:12px;top:140px;width:118px"><p>Our adjusters examine each loss on site, gather the facts and prepare a clear report, so insurers and brokers can settle the claim quickly and fairly for every client.</p><p class="lead">Fast, precise assessments with a single contact from the first notice to the final settlement.</p></div>
    <div class="col" style="left:142px;top:140px;width:118px"><p class="lead">Fast, precise assessments with a single contact from the first notice to the final settlement.</p><p>Our adjusters examine each loss on site, gather the facts and prepare a clear report, so insurers and brokers can settle the claim quickly and fairly for every client.</p></div>
    <div class="foot"><span class="num">05</span><span>www.tavesidurando.it</span><span class="brand">Tavesi and Durando</span></div>
  </div>
  <div class="page right">
    <div class="mark">SERVICES</div>
    <div class="title" style="left:12px;top:26px">TELECLAIMER</div>
    <div class="title" style="left:142px;top:26px">AUDITING</div>
    <div class="photo" role="img" aria-label="Operatrice con cuffie al telefono" style="left:12px;top:40px;width:118px;height:55px;background:linear-gradient(135deg,#e7d9cc,#9a8778)"></div>
    <div class="photo" role="img" aria-label="Mano che seleziona l'icona audit" style="left:142px;top:40px;width:120px;height:55px;background:linear-gradient(135deg,#1f5f8f,#9fc7df)"></div>
    <div class="intro" style="left:12px;top:100px;width:118px">Fast, precise assessments with a single contact from the first notice.</div>
    <div class="intro" style="left:142px;top:100px;width:120px">Fast, precise assessments with a single contact from the first notice.</div>
    <div class="col" style="left:12px;top:122px;width:118px"><p>Our adjusters examine each loss on site, gather the facts and prepare a clear report, so insurers and brokers can settle the claim quickly and fairly for every client.</p><p class="lead">Fast, precise assessments with a single contact from the first notice to the final settlement.</p><p>Every file is followed by a dedicated expert and tracked in real time.</p></div>
    <div class="col" style="left:142px;top:122px;width:120px"><p>Our adjusters examine each loss on site, gather the facts and prepare a clear report, so insurers and brokers can settle the claim quickly and fairly for every client.</p><p class="lead">Fast, precise assessments with a single contact from the first notice to the final settlement.</p><p>Every file is followed by a dedicated expert and tracked in real time.</p></div>
    <div class="foot"><span class="brand">Tavesi and Durando</span><span>www.tavesidurando.it</span><span class="num">06</span></div>
  </div>
</div>

<div class="spread" style="left:608px;top:1140px">
  <div class="page left">
    <div class="mark" style="left:50px">SPECIALIZATIONS</div>
    <div class="title" style="left:12px;top:26px">TECNOLOGICI</div>
    <div class="photo" role="img" aria-label="Cavi di rete collegati a un server" style="left:12px;top:40px;width:118px;height:200px;background:linear-gradient(180deg,#0d3c6b,#3aa0d8 60%,#0b2c4e)"></div>
    <div class="col" style="left:140px;top:40px;width:120px"><p class="lead">Fast, precise assessments with a single contact from the first notice to the final settlement.</p><p>Our adjusters examine each loss on site, gather the facts and prepare a clear report, so insurers and brokers can settle the claim quickly and fairly for every client.</p><p class="lead">Fast, precise assessments with a single contact from the first notice to the final settlement.</p></div>
    <div class="box blue" style="left:12px;top:250px;width:250px;height:75px">Our adjusters examine each loss on site, gather the facts and prepare a clear report, so insurers and brokers can settle the claim quickly and fairly for every client.</div>
    <div class="foot"><span class="num">15</span><span>www.tavesidurando.it</span><span class="brand">Tavesi and Durando</span></div>
  </div>
  <div class="page right">
    <div class="mark">SPECIALIZATIONS</div>
    <div class="title" style="left:12px;top:26px">STRUTTURE</div>
    <div class="photo" role="img" aria-label="Capannone industriale in costruzione" style="left:12px;top:40px;width:250px;height:75px;background:linear-gradient(135deg,#b59a7a,#5b4a3a)"></div>
    <div class="box orange" style="left:140px;top:100px;width:122px;height:60px">Our adjusters examine each loss on site, gather the facts and prepare a clear report for every client.</div>
    <div class="col" style="left:12px;top:122px;width:118px"><p>Our adjusters examine each loss on site, gather the facts and prepare a clear report, so insurers and brokers can settle the claim quickly and fairly for every client.</p><p class="lead">Fast, precise assessments with a single contact from the first notice to the final settlement.</p><p>Every file is followed by a dedicated expert and tracked in real time.</p></div>
    <div class="photo" role="img" aria-label="Struttura in legno di una casa" style="left:140px;top:170px;width:122px;height:60px;background:linear-gradient(135deg,#e0c9a4,#8c6a44)"></div>
    <div class="col" style="left:140px;top:238px;width:122px"><p>Our adjusters examine each loss on site, gather the facts and prepare a clear report.</p></div>
    <div class="foot"><span class="brand">Tavesi and Durando</span><span>www.tavesidurando.it</span><span class="num">16</span></div>
  </div>
</div>

<div class="spread" style="left:38px;top:1508px">
  <div class="page left">
    <div class="mark">SERVICES</div>
    <div class="title small" style="left:12px;top:27px">ACCERTAMENTO DANNI DA FENOMENO ELETTRICO</div>
    <div class="photo" role="img" aria-label="Fulmine in un cielo blu" style="left:12px;top:40px;width:250px;height:75px;background:linear-gradient(135deg,#0e2a5c,#4f8fd6 55%,#0a1d3f)"></div>
    <div class="intro" style="left:12px;top:120px;width:250px">Fast, precise assessments with a single contact from the first notice to the final settlement.</div>
    <div class="col" style="left:12px;top:140px;width:118px"><p>Our adjusters examine each loss on site, gather the facts and prepare a clear report, so insurers and brokers can settle the claim quickly and fairly for every client.</p><p class="lead">Fast, precise assessments with a single contact from the first notice to the final settlement.</p></div>
    <div class="col" style="left:142px;top:140px;width:118px"><p class="lead">Fast, precise assessments with a single contact from the first notice to the final settlement.</p><p>Our adjusters examine each loss on site, gather the facts and prepare a clear report, so insurers and brokers can settle the claim quickly and fairly for every client.</p></div>
    <div class="foot"><span class="num">07</span><span>www.tavesidurando.it</span><span class="brand">Tavesi and Durando</span></div>
  </div>
  <div class="page right">
    <div class="mark">SERVICES</div>
    <div class="title" style="left:12px;top:26px">TPA</div>
    <div class="photo" role="img" aria-label="Penna su un documento contrattuale" style="left:12px;top:40px;width:250px;height:75px;background:linear-gradient(135deg,#26323e,#8797a6)"></div>
    <div class="intro" style="left:12px;top:122px;width:118px">Fast, precise assessments with a single contact from the first notice to the final settlement.</div>
    <div class="col" style="left:12px;top:150px;width:118px"><p>Our adjusters examine each loss on site, gather the facts and prepare a clear report, so insurers and brokers can settle the claim quickly and fairly for every client.</p><p class="lead">Fast, precise assessments with a single contact from the first notice to the final settlement.</p></div>
    <div class="col" style="left:142px;top:122px;width:120px"><p class="lead">Fast, precise assessments with a single contact from the first notice to the final settlement.</p><p>Our adjusters examine each loss on site, gather the facts and prepare a clear report, so insurers and brokers can settle the claim quickly and fairly for every client.</p><p>Every file is followed by a dedicated expert and tracked in real time.</p></div>
    <div class="foot"><span class="brand">Tavesi and Durando</span><span>www.tavesidurando.it</span><span class="num">08</span></div>
  </div>
</div>

<div class="spread" style="left:608px;top:1508px">
  <div class="page left">
    <div class="mark" style="left:50px">SPECIALIZATIONS</div>
    <div class="title" style="left:12px;top:26px">AMBIENTE</div>
    <div class="photo" role="img" aria-label="Mani che reggono un globo verde" style="left:12px;top:40px;width:118px;height:110px;background:linear-gradient(135deg,#2e7d32,#a5d6a7)"></div>
    <div class="col" style="left:140px;top:40px;width:120px"><p class="lead">Fast, precise assessments with a single contact from the first notice to the final settlement.</p><p>Our adjusters examine each loss on site, gather the facts and prepare a clear report, so insurers and brokers can settle the claim quickly and fairly for every client.</p></div>
    <div class="box blue" style="left:12px;top:160px;width:250px;height:40px">Our adjusters examine each loss on site, gather the facts and prepare a clear report for every client.</div>
    <div class="col" style="left:12px;top:208px;width:118px"><p>Our adjusters examine each loss on site, gather the facts and prepare a clear report, so insurers and brokers can settle the claim quickly.</p></div>
    <div class="col" style="left:140px;top:208px;width:120px"><p class="lead">Fast, precise assessments with a single contact from the first notice to the final settlement.</p><p>Every file is followed by a dedicated expert and tracked in real time.</p></div>
    <div class="foot"><span class="num">17</span><span>www.tavesidurando.it</span><span class="brand">Tavesi and Durando</span></div>
  </div>
  <div class="page right">
    <div class="band title-band" style="left:0;top:10px;width:273px">INTEGRATED SERVICES</div>
    <div class="title" style="left:12px;top:44px">PERDITE OCCULTE</div>
    <div class="title" style="left:142px;top:44px">RICERCA GUASTI</div>
    <div class="photo" role="img" aria-label="Tubo che perde acqua" style="left:12px;top:58px;width:118px;height:55px;background:linear-gradient(135deg,#7ab6d9,#1f5777)"></div>
    <div class="photo" role="img" aria-label="Tecnico con strumento di misura" style="left:142px;top:58px;width:120px;height:55px;background:linear-gradient(135deg,#cfa57a,#5c4636)"></div>
    <div class="intro" style="left:12px;top:118px;width:118px">Fast, precise assessments with a single contact from the first notice.</div>
    <div class="intro" style="left:142px;top:118px;width:120px">Fast, precise assessments with a single contact from the first notice.</div>
    <div class="col" style="left:12px;top:140px;width:118px"><p>Our adjusters examine each loss on site, gather the facts and prepare a clear report, so insurers and brokers can settle the claim quickly and fairly for every client.</p><p class="lead">Fast, precise assessments with a single contact from the first notice to the final settlement.</p></div>
    <div class="col" style="left:142px;top:140px;width:120px"><p>Our adjusters examine each loss on site, gather the facts and prepare a clear report, so insurers and brokers can settle the claim quickly and fairly for every client.</p><p class="lead">Fast, precise assessments with a single contact from the first notice to the final settlement.</p></div>
    <div class="foot"><span class="brand">Tavesi and Durando</span><span>www.tavesidurando.it</span><span class="num">18</span></div>
  </div>
</div>

<div class="spread" style="left:38px;top:1875px">
  <div class="page left">
    <div class="mark">SERVICES</div>
    <div class="title" style="left:12px;top:26px">DRONE PILOT</div>
    <div class="box orange" style="left:12px;top:40px;width:75px;height:80px">Our adjusters examine each loss on site and prepare a clear report.</div>
    <div class="photo" role="img" aria-label="Pilota con drone in volo" style="left:90px;top:40px;width:172px;height:80px;background:linear-gradient(135deg,#9aa6b0,#3c4650)"></div>
    <div class="band" style="left:0;top:130px;width:273px;height:110px"></div>
    <div class="col on-blue" style="left:12px;top:138px;width:118px"><p>Our adjusters examine each loss on site, gather the facts and prepare a clear report, so insurers and brokers can settle the claim quickly.</p><p class="lead">Fast, precise assessments with a single contact from the first notice to the final settlement.</p></div>
    <div class="col on-blue" style="left:142px;top:138px;width:118px"><p class="lead">Fast, precise assessments with a single contact from the first notice to the final settlement.</p><p>Every file is followed by a dedicated expert and tracked in real time.</p></div>
    <div class="col" style="left:12px;top:250px;width:250px"><p>Our adjusters examine each loss on site, gather the facts and prepare a clear report, so insurers and brokers can settle the claim quickly and fairly for every client.</p></div>
    <div class="foot"><span class="num">09</span><span>www.tavesidurando.it</span><span class="brand">Tavesi and Durando</span></div>
  </div>
  <div class="page right">
    <div class="mark">SERVICES</div>
    <div class="title" style="left:12px;top:26px">VALUTAZIONE RISCHI</div>
    <div class="photo" role="img" aria-label="Modulo di valutazione del rischio con penna" style="left:12px;top:40px;width:250px;height:75px;background:linear-gradient(135deg,#f2f2f2,#a7a7a7)"></div>
    <div class="intro" style="left:12px;top:120px;width:250px">Fast, precise assessments with a single contact from the first notice to the final settlement.</div>
    <div class="col" style="left:12px;top:140px;width:118px"><p>Our adjusters examine each loss on site, gather the facts and prepare a clear report, so insurers and brokers can settle the claim quickly and fairly for every client.</p><p class="lead">Fast, precise assessments with a single contact from the first notice to the final settlement.</p></div>
    <div class="col" style="left:142px;top:140px;width:118px"><p class="lead">Fast, precise assessments with a single contact from the first notice to the final settlement.</p><p>Our adjusters examine each loss on site, gather the facts and prepare a clear report, so insurers and brokers can settle the claim quickly and fairly for every client.</p></div>
    <div class="foot"><span class="brand">Tavesi and Durando</span><span>www.tavesidurando.it</span><span class="num">10</span></div>
  </div>
</div>

<div class="spread" style="left:608px;top:1875px">
  <div class="page left">
    <div class="title small" style="left:12px;top:13px">INDAGINI TERMOGRAFICHE</div>
    <div class="title small" style="left:142px;top:13px">CRISIS MANAGEMENT</div>
    <div class="photo" role="img" aria-label="Immagine termografica di un edificio" style="left:12px;top:26px;width:118px;height:60px;background:linear-gradient(135deg,#2a3fbf,#e53935 50%,#ffeb3b)"></div>
    <div class="photo" role="img" aria-label="Illustrazione di salvagente sulle onde" style="left:142px;top:26px;width:120px;height:60px;background:linear-gradient(180deg,#e9f3f7,#4fa3c9)"></div>
    <div class="intro" style="left:12px;top:92px;width:118px">Fast, precise assessments with a single contact from the first notice.</div>
    <div class="intro" style="left:142px;top:92px;width:120px">Fast, precise assessments with a single contact from the first notice.</div>
    <div class="col" style="left:12px;top:114px;width:118px"><p>Our adjusters examine each loss on site, gather the facts and prepare a clear report, so insurers and brokers can settle the claim quickly and fairly for every client.</p><p class="lead">Fast, precise assessments with a single contact from the first notice to the final settlement.</p><p>Every file is followed by a dedicated expert and tracked in real time.</p></div>
    <div class="col" style="left:142px;top:114px;width:120px"><p>Our adjusters examine each loss on site, gather the facts and prepare a clear report, so insurers and brokers can settle the claim quickly and fairly for every client.</p><p class="lead">Fast, precise assessments with a single contact from the first notice to the final settlement.</p></div>
    <div class="foot"><span class="num">19</span><span>www.tavesidurando.it</span><span class="brand">Tavesi and Durando</span></div>
  </div>
  <div class="page right">
    <div class="title" style="left:12px;top:12px">LE MANDANTI</div>
    <div class="clients">
      <span>Norvalia</span><span>Pellisco</span><span>Tamberi</span><span></span>
      <span>Dorvane</span><span>Castelmo</span><span>Ferrante</span><span></span>
      <span>Lusigna</span><span>Moravel</span><span>Quintaro</span><span>Serbelli</span>
      <span></span><span>Varenza</span><span></span><span></span>
    </div>
    <div class="box blue" style="left:12px;top:205px;width:72px;height:95px">La Struttura opera su tutte le province della Lombardia, Emilia Romagna e territorio nazionale.</div>
    <div class="photo" role="img" aria-label="Mappa delle regioni del nord Italia" style="left:90px;top:205px;width:172px;height:95px;background:linear-gradient(135deg,#e6eef3,#b0c4d2)"></div>
    <div class="col" style="left:12px;top:306px;width:250px"><p>Every file is followed by a dedicated expert and tracked in real time.</p></div>
    <div class="foot"><span class="brand">Tavesi and Durando</span><span>www.tavesidurando.it</span><span class="num">20</span></div>
  </div>
</div>

</body>
</html>
```